Business Card Design for New Game Studio

We need a business card design. We are a new company developing innovative mobile and platform games.

I would like to see very innovative design thats brings out the company's goal and direction.

My Company's goal and direction is to "Evolve the way of gaming, Bring fun and entertainment to all gamers"

Please do use our company logo which I have attached to be included in the design.

Please put in details for name, title, contacts etc ... be creative !!!

Reason: Company logo redesign. Awaiting it. Thanks

Hi all Please do wait for my updated company logo. Thanks

Reason: Still waiting on new company logo. Thanks all

Hi All Designers .... Sorry for the long wait... Please see the new file for my new company logo uploaded. Waiting to see all your creative design. Cheers

Hi All .... Please do not just mass send a whole bunch of similar designs .... Would like to see quality instead of quantity Cheers

Entertainment

```html
<!DOCTYPE html>
<html lang="en">
<head>
<meta charset="utf-8">
<title>Novaform Play – Business Card</title>
<link href="https://fonts.googleapis.com/css2?family=Open+Sans:wght@400;600;700&display=swap" rel="stylesheet">
<style>
  :root {
    --lime: #c9de2a;
    --ink: #0b0b0b;
    --ink-soft: #2f2f2b;
    --paper: #ffffff;
    --grey-text: #d9d9d9;
    --rule: #3b3b3b;
    --backdrop: #e9e9ec;
  }
  * { margin: 0; padding: 0; box-sizing: border-box; }
  html, body {
    width: 1200px; height: 987px; overflow: hidden;
    background: var(--backdrop);
    font-family: "Open Sans", sans-serif;
  }
  .stage { position: relative; width: 1200px; height: 987px; }
  .card {
    position: absolute; top: 340px;
    width: 540px; height: 308px;
    border-radius: 26px; overflow: hidden;
  }
  .card--front { left: 40px; background: var(--ink); }
  .card--back  { left: 620px; background: var(--lime); }

  .card__waves { position: absolute; inset: 0; width: 100%; height: 100%; }

  .brand {
    position: absolute; left: 30px; top: 82px;
    display: flex; align-items: center; gap: 10px;
    color: var(--lime); font-weight: 700; font-size: 22px;
    white-space: nowrap;
  }
  .brand__dot { width: 12px; height: 12px; background: var(--lime); flex: none; }

  .divider {
    position: absolute; left: 262px; top: 30px;
    width: 1px; height: 150px; background: var(--rule);
  }

  .contact { position: absolute; left: 284px; top: 26px; color: var(--paper); }
  .contact__name { color: var(--lime); font-weight: 600; font-size: 22px; line-height: 1.15; }
  .contact__title { color: var(--grey-text); font-size: 13px; margin-bottom: 10px; }
  .contact__list { list-style: none; }
  .contact__item {
    display: flex; align-items: center; gap: 8px;
    font-size: 14px; line-height: 22px; white-space: nowrap;
  }
  .contact__item svg { width: 13px; height: 13px; flex: none; }

  .address {
    position: absolute; right: 24px; bottom: 10px;
    color: var(--ink-soft); font-size: 13px; font-weight: 600;
    line-height: 1.3; text-align: right;
  }

  .tagline {
    position: absolute; inset: 0;
    display: flex; flex-direction: column; justify-content: center; align-items: center;
    text-align: center; color: var(--ink-soft);
  }
  .tagline__text { font-size: 21px; line-height: 1.3; }
  .tagline__url { font-size: 20px; margin-top: 14px; letter-spacing: 1px; }
</style>
</head>
<body>
<main class="stage">

  <section class="card card--front" aria-label="Business card front">
    <svg class="card__waves" viewBox="0 0 540 308" aria-hidden="true">
      <path d="M0 110 C 5 200, 60 210, 160 215 C 300 222, 450 235, 540 258 L 540 308 L 0 308 Z" fill="var(--lime)"/>
      <path d="M8 135 C 25 215, 90 230, 190 238 C 270 246, 320 275, 340 308"
            fill="none" stroke="var(--ink)" stroke-width="5"/>
    </svg>

    <div class="brand">
      <span class="brand__dot"></span>
      <span class="brand__name">Novaform Play</span>
    </div>

    <div class="divider"></div>

    <div class="contact">
      <p class="contact__name">Your Name</p>
      <p class="contact__title">Title</p>
      <ul class="contact__list">
        <li class="contact__item">
          <svg viewBox="0 0 16 16"><circle cx="8" cy="8" r="7.5" fill="var(--lime)"/><path d="M5 4.5l2 1.5-1 1.5a6 6 0 0 0 2.5 2.5l1.5-1 1.5 2-1.5 1C7 12 4 9 4 6z" fill="var(--ink)"/></svg>
          012-345-6789
        </li>
        <li class="contact__item">
          <svg viewBox="0 0 16 16"><rect x="4" y="1" width="8" height="14" rx="1.5" fill="var(--lime)"/><rect x="5.5" y="3" width="5" height="6" fill="var(--ink)"/></svg>
          012-345-6789
        </li>
        <li class="contact__item">
          <svg viewBox="0 0 16 16"><rect x="1" y="3" width="14" height="10" rx="1" fill="var(--lime)"/><path d="M1 4l7 5 7-5" fill="none" stroke="var(--ink)" stroke-width="1.2"/></svg>
          info@novaformplay.com
        </li>
        <li class="contact__item">
          <svg viewBox="0 0 16 16"><circle cx="8" cy="8" r="7" fill="var(--lime)"/><g fill="none" stroke="var(--ink)" stroke-width="0.9"><ellipse cx="8" cy="8" rx="3" ry="7"/><path d="M1 8h14M2.5 4.5h11M2.5 11.5h11"/></g></svg>
          www.novaformplay.com
        </li>
      </ul>
    </div>

    <p class="address">Street Name, City Name<br>Zip Code - 000000</p>
  </section>

  <section class="card card--back" aria-label="Business card back">
    <div class="tagline">
      <p class="tagline__text">Evolve The Way Of Gaming<br>Bring Fun And<br>Entertainment To All Gamers</p>
      <p class="tagline__url">www.novaformplay.com</p>
    </div>
  </section>

</main>
</body>
</html>
```